Website for new child psychology practice

New clinical psychology practice in NSW Australia, specialising in work with children, adolescents and families. I would like to feature the colours in the logo, which was recently designed by pixelmesa designer Odette.
I am seeking a professional looking page, which is easy to navigate and is colourful and playful but not childish.
Target Market(s)
Parents and professionals
Industry/Entity Type
Health
Coding
Coded - Design and coding required
Number of Pages Required
1 page
Font styles to use
Serif
Requirements
Must have
- Pages for 'About us' 'Services' 'Fees and information' 'Contact us'
Should not have
- Childish stock photos

```html
<!DOCTYPE html>
<html lang="en">
<head>
<meta charset="utf-8">
<title>Dr Clara Vance – Clinical Psychology Practice</title>
<link href="https://fonts.googleapis.com/css2?family=Cinzel:wght@400;600&family=Poppins:wght@400;500;600&display=swap" rel="stylesheet">
<style>
:root{
  --plum:#7d2462;
  --magenta:#a6298f;
  --pink:#c86bb0;
  --orange:#ec7a3c;
  --amber:#f6b24a;
  --red:#e0463a;
  --ink:#1d1a1f;
  --body:#3c3640;
  --blush:#f6e6ea;
  --lavender:#eedbec;
  --serif:'Cinzel',serif;
  --sans:'Poppins',sans-serif;
}
*{box-sizing:border-box;margin:0;padding:0}
html,body{width:1200px;height:4027px;overflow:hidden}
body{position:relative;background:#fff;font-family:var(--sans);color:var(--body)}
.abs{position:absolute}
a{color:inherit;text-decoration:none}

/* header */
.topbar{left:0;top:0;width:1200px;height:5px;background:linear-gradient(90deg,var(--magenta),var(--orange),var(--magenta))}
.brand{display:flex;align-items:center;gap:10px;font-family:var(--serif);font-weight:600;color:var(--plum);font-size:28px;letter-spacing:1px}
.brand-dot{width:34px;height:34px;border-radius:50%;background:var(--magenta)}
.nav{left:476px;top:40px;display:flex;gap:42px;font-family:var(--serif);font-size:14px;color:var(--ink);letter-spacing:.5px}
.nav a.active{border-bottom:2px solid var(--magenta);padding-bottom:10px}
.btn{display:inline-flex;align-items:center;justify-content:center;border-radius:30px;color:#fff;font-family:var(--serif);font-size:15px;letter-spacing:1px}
.btn-contact{left:919px;top:28px;width:156px;height:44px;background:var(--magenta);font-size:14px}

/* hero */
.hero{left:0;top:0;width:1200px;height:700px;background:linear-gradient(180deg,#f7eef6 0%,var(--lavender) 70%)}
.hero-kicker{left:128px;top:212px;font-family:var(--serif);font-size:22px;color:var(--ink);letter-spacing:1px}
.kicker-line{left:0;top:225px;width:112px;height:2px;background:var(--magenta)}
.hero-title{left:122px;top:238px;font-family:var(--serif);font-weight:600;font-size:56px;line-height:50px;letter-spacing:3px;color:var(--ink)}
.hero-title .p{color:var(--magenta)} .hero-title .o{color:var(--orange)}
.btn-schedule{left:122px;top:422px;width:280px;height:50px;background:linear-gradient(90deg,var(--orange),var(--red));justify-content:flex-start;padding-left:30px;font-size:14px}
.btn-schedule .bubble{position:absolute;right:-4px;top:-4px;width:56px;height:56px;border-radius:50%;background:var(--magenta);border:5px solid #fff}
.hero-art{left:570px;top:140px;width:524px;height:438px;border-radius:48% 52% 46% 54%;background:radial-gradient(circle at 40% 40%,var(--amber),var(--orange) 35%,var(--magenta) 65%,var(--plum) 90%);opacity:.9}

/* about */
.about-ring{left:97px;top:750px;width:468px;height:468px;border-radius:50%;background:conic-gradient(var(--amber) 0 55%,var(--magenta) 55% 100%)}
.about-photo{left:119px;top:772px;width:436px;height:436px;border-radius:50%;background:linear-gradient(160deg,#d8c2b4,#8f8790 60%,#5d5865)}
.eyebrow{font-family:var(--serif);font-size:22px;letter-spacing:2px}
.about-eyebrow{left:608px;top:817px;color:var(--magenta)}
.about-title{left:608px;top:843px;font-family:var(--serif);font-size:48px;letter-spacing:2px;color:var(--ink)}
.about-line{left:1088px;top:866px;width:112px;height:2px;background:var(--magenta)}
.about-text{left:615px;top:910px;width:470px;font-size:16.5px;line-height:27px;color:var(--body)}
.about-text p+p{margin-top:27px}
.btn-learn{left:608px;top:1125px;width:190px;height:48px;background:linear-gradient(90deg,var(--red),var(--orange))}

/* services */
.services-bg{left:0;top:1280px;width:1200px;height:640px}
.services-eyebrow{left:0;top:1370px;width:1200px;text-align:center;color:var(--amber);font-size:20px}
.services-title{left:0;top:1393px;width:1200px;text-align:center;font-family:var(--serif);font-size:42px;letter-spacing:2px;color:#fff}
.services-rule{left:553px;top:1446px;width:94px;height:2px;background:var(--amber)}
.service{width:344px;height:344px;border-radius:50%;border:4px solid #fff;display:flex;flex-direction:column;align-items:center;padding-top:36px;text-align:center;color:#fff}
.service.featured{background:var(--pink);border-color:var(--pink)}
.service-icon{width:98px;height:92px;border-radius:50% 50% 50% 8%;margin-bottom:22px}
.service h3{font-family:var(--serif);font-weight:400;font-size:22px;letter-spacing:1px;margin-bottom:10px}
.service p{width:230px;font-size:11.5px;line-height:20px;color:#f3dcec;margin-bottom:16px}
.service .pill{border:2px solid #fff;border-radius:24px;width:144px;height:36px;display:flex;align-items:center;justify-content:center;font-family:var(--serif);font-size:12px;letter-spacing:1px}

/* fees */
.fees-bg{left:0;top:1906px;width:1200px;height:589px;background:linear-gradient(90deg,#fbeef0,var(--blush))}
.fees-photo{left:500px;top:1867px;width:700px;height:628px;background:linear-gradient(120deg,#efe4e2 0%,#d9cfd2 35%,#9aa6a1 70%,#c6b6b5 100%)}
.fees-eyebrow{left:144px;top:2000px;color:var(--magenta)}
.fees-title{left:144px;top:2025px;font-family:var(--serif);font-size:48px;letter-spacing:3px;color:var(--ink)}
.fees-rule{left:148px;top:2086px;width:70px;height:2px;background:linear-gradient(90deg,var(--magenta) 10%,#ddd 10%)}
.fees-text{left:147px;top:2115px;width:364px;font-size:14.5px;line-height:23px;text-align:justify}
.fees-text p+p{margin-top:22px}
.btn-fees{left:148px;top:2297px;width:175px;height:47px;background:var(--magenta)}

/* testimonials */
.t-eyebrow{left:0;top:2560px;width:1200px;text-align:center;color:var(--magenta);font-size:18px}
.t-title{left:0;top:2578px;width:1200px;text-align:center;font-family:var(--serif);font-size:40px;letter-spacing:3px;color:var(--ink)}
.card{top:2667px;width:310px;height:250px;border:1.5px solid #e3c6dd;padding:36px 30px 0 34px}
.card p{font-size:13px;line-height:22px;color:var(--body)}
.reviewer{position:absolute;left:32px;bottom:28px;display:flex;gap:10px;align-items:center}
.avatar{width:36px;height:36px;border-radius:50%;background:linear-gradient(135deg,#d8b9a4,#8c7a75)}
.reviewer b{display:block;font-size:12.5px;color:var(--ink);font-weight:600}
.stars{color:var(--amber);font-size:14px;letter-spacing:2px}
.source{position:absolute;right:22px;bottom:28px;width:24px;height:24px;border-radius:50%;background:#d9d4dc}
.arrow{top:2770px}

/* contact */
.contact-bg{left:0;top:2990px;width:1200px;height:650px}
.contact-eyebrow{left:144px;top:3084px;color:var(--amber);font-size:20px}
.contact-line{left:0;top:3125px;width:108px;height:2px;background:var(--amber)}
.contact-title{left:144px;top:3105px;font-family:var(--serif);font-size:42px;letter-spacing:3px;color:#fff}
.field{left:144px;width:411px;background:#fff;font-size:13px;color:var(--ink);padding:12px 20px;font-weight:500}
.btn-send{left:144px;top:3441px;width:187px;height:45px;background:var(--plum);font-family:var(--sans);font-weight:600;font-size:13px;letter-spacing:0}
.contact-art{left:640px;top:3086px;width:454px;height:484px;border-radius:46% 54% 50% 50%;background:radial-gradient(circle at 70% 30%,#d9a3d7,var(--magenta) 40%,transparent 72%),radial-gradient(circle at 25% 70%,var(--amber),transparent 45%),radial-gradient(circle at 30% 25%,#5a4a4f,transparent 40%),radial-gradient(circle at 65% 80%,#3f4d6b,transparent 40%)}

/* footer */
.footer-brand{left:150px;top:3735px;width:294px;justify-content:center}
.socials{left:222px;top:3802px;display:flex;gap:6px}
.socials span{width:44px;height:44px;border-radius:50%;background:var(--magenta)}
.divider{top:3625px;width:1px;height:325px;background:#e6d6e2}
.f-head{font-family:var(--serif);font-size:22px;color:var(--plum);letter-spacing:1px;border-left:3px solid var(--magenta);padding-left:30px}
.f-links{left:548px;top:3737px;list-style:none;font-size:13.5px;color:var(--ink);line-height:27px}
.f-contact{left:780px;top:3740px}
.f-row{display:flex;gap:12px;align-items:center;font-size:14px;color:var(--ink);line-height:22px;margin-bottom:26px}
.f-icon{width:44px;height:44px;border-radius:50% 50% 50% 10%;background:#e88bb3;display:flex;align-items:center;justify-content:center}
.footer-rule{left:0;top:3950px;width:1200px;height:1px;background:#e6d6e2}
.copyright{left:0;top:3972px;width:1200px;text-align:center;font-size:12px;color:#555}
</style>
</head>
<body>

<!-- hero -->
<section class="hero abs"></section>
<svg class="abs" style="left:0;top:560px" width="1200" height="160" viewBox="0 0 1200 160">
  <path d="M0 130 C 300 150 600 150 860 100 C 1000 70 1120 40 1200 18 L1200 160 L0 160 Z" fill="#fff"/>
  <path d="M0 130 C 300 148 600 148 860 98 C 1000 70 1120 40 1200 18 L1200 54 C 1100 80 980 110 860 118 C 600 150 300 148 0 132 Z" fill="var(--magenta)"/>
</svg>
<div class="topbar abs"></div>
<div class="brand abs" style="left:98px;top:28px"><span class="brand-dot"></span>Dr Clara Vance</div>
<nav class="nav abs">
  <a class="active" href="#about">About Us</a><a href="#services">Services</a><a href="#fees">Fees &amp; Information</a>
</nav>
<a class="btn btn-contact abs" href="#contact">Contact Us</a>

<div class="kicker-line abs"></div>
<div class="hero-kicker abs">Dr Clara Vance</div>
<h1 class="hero-title abs">Clinical<br><span class="p">Psychology</span><br><span class="o">Practice</span></h1>
<a class="btn btn-schedule abs" href="#contact">Schedule Appointment<span class="bubble"></span></a>
<div class="hero-art abs" role="img" aria-label="Cluster of colourful speech bubbles with tree and landscape imagery"></div>

<!-- about -->
<svg class="abs" style="left:0;top:690px" width="260" height="260" viewBox="0 0 260 260" fill="none" stroke="#e4e0e6" stroke-width="1">
  <path d="M0 20 C80 10 160 40 200 120 C230 180 240 220 260 260"/><path d="M0 35 C80 25 150 55 190 130 C220 190 225 225 240 260"/><path d="M0 50 C70 42 140 70 180 140 C205 195 210 230 220 260"/><path d="M0 65 C60 60 130 85 165 150 C190 200 195 230 200 260"/>
</svg>
<div class="about-ring abs"></div>
<div class="about-photo abs" role="img" aria-label="Portrait photo of the psychologist holding a notepad"></div>
<div class="eyebrow about-eyebrow abs" id="about">About Us</div>
<h2 class="about-title abs">Dr Clara Vance</h2>
<div class="about-line abs"></div>
<div class="about-text abs">
  <p>Lorem ipsum dolor sit amet, consectetur adipiscing elit, sed do eiusmod tempor incididunt ut labore et dolore magna aliqua. Quis ipsum suspendisse ultrices gravida. Risus commodo viverra maecenas accumsa</p>
  <p>Lorem ipsum dolor sit amet, consectetur adipiscing elit, sed do eiusmod tempor incididunt ut labore et dolore</p>
</div>
<a class="btn btn-learn abs" href="#about">Learn More</a>

<!-- services -->
<svg class="services-bg abs" viewBox="0 0 1200 640" preserveAspectRatio="none">
  <defs><linearGradient id="svcGrad" x1="0" y1="0" x2="1" y2="0"><stop offset="0" stop-color="#a6298f"/><stop offset="1" stop-color="#7d2462"/></linearGradient></defs>
  <path d="M0 20 C 300 -10 700 10 1200 20 L1200 560 C 800 620 300 640 0 620 Z" fill="url(#svcGrad)"/>
  <path d="M0 50 C 250 0 650 -2 1200 20 L1200 0 C 700 -10 250 0 0 20 Z" fill="var(--amber)"/>
  <path d="M0 620 C 400 640 800 620 1200 540 L1200 580 C 800 640 400 650 0 640 Z" fill="var(--orange)"/>
</svg>
<div class="eyebrow services-eyebrow abs" id="services">What We Do</div>
<h2 class="services-title abs">Services Provide</h2>
<div class="services-rule abs"></div>
<div class="service abs" style="left:122px;top:1480px">
  <div class="service-icon" style="background:#d99bc7" role="img" aria-label="Head with brain icon"></div>
  <h3>Services Heading</h3>
  <p>Lorem ipsum dolor sit amet, consectetur adipiscing elit, sed do eiusmod teLorem ipsum dolor sit</p>
  <span class="pill">Learn More</span>
</div>
<div class="service featured abs" style="left:426px;top:1480px">
  <div class="service-icon" style="background:var(--plum)" role="img" aria-label="Head with connected ideas icon"></div>
  <h3>Services Heading</h3>
  <p>Lorem ipsum dolor sit amet, consectetur adipiscing elit, sed do eiusmod teLorem ipsum dolor sit</p>
  <span class="pill">Learn More</span>
</div>
<div class="service abs" style="left:731px;top:1469px">
  <div class="service-icon" style="background:var(--amber)" role="img" aria-label="Head with gears icon"></div>
  <h3>Services Heading</h3>
  <p>Lorem ipsum dolor sit amet, consectetur adipiscing elit, sed do eiusmod teLorem ipsum dolor sit</p>
  <span class="pill">Learn More</span>
</div>

<!-- fees -->
<div class="fees-bg abs"></div>
<div class="fees-photo abs" role="img" aria-label="Photo of a psychologist with a clipboard talking with a young client"></div>
<div class="eyebrow fees-eyebrow abs" id="fees">Fee &amp; Information</div>
<h2 class="fees-title abs">Our Fees</h2>
<div class="fees-rule abs"></div>
<div class="fees-text abs">
  <p>Lorem ipsum dolor sit amet, consectetur adipiscing elit, sed do eiusmod tempor incididunt ut labore</p>
  <p>At dolore magna aliqua. Quis ipsum suspendisse ultrices Lorem ipsum dolor sit amet, consectetur adipiscing elit, sed do eiusmod tempor incididunt ut labore et dolore ultrices Lorem ipsum dolor sit</p>
</div>
<a class="btn btn-fees abs" href="#fees">Learn More</a>

<!-- testimonials -->
<div class="eyebrow t-eyebrow abs">People Words</div>
<h2 class="t-title abs">Testimonials</h2>
<svg class="arrow abs" style="left:74px" width="24" height="36" viewBox="0 0 24 36"><path d="M18 4 L6 18 L18 32" fill="none" stroke="var(--magenta)" stroke-width="3"/></svg>
<svg class="arrow abs" style="left:1128px" width="24" height="36" viewBox="0 0 24 36"><path d="M6 4 L18 18 L6 32" fill="none" stroke="var(--magenta)" stroke-width="3"/></svg>
<article class="card abs" style="left:123px">
  <p>Lorem ipsum dolor sit amet, consectetur adipiscing elit, sed do eiusmod tempor incididunt ut labore et dolore magna aliqua. Quis ipsum suspendisse ultrices gravida. Risus commodo viverra maecenas acc</p>
  <div class="reviewer"><span class="avatar"></span><div><b>Robert Jameson</b><span class="stars">★★★★★</span></div></div>
  <span class="source"></span>
</article>
<article class="card abs" style="left:456px">
  <p>Lorem ipsum dolor sit amet, consectetur adipiscing elit, sed do eiusmod tempor incididunt ut labore et dolore magna aliqua. Quis ipsum suspendisse ultrices gravida. Risus commodo viverra maecenas acc</p>
  <div class="reviewer"><span class="avatar"></span><div><b>Robert Jameson</b><span class="stars">★★★★★</span></div></div>
  <span class="source"></span>
</article>
<article class="card abs" style="left:788px">
  <p>Lorem ipsum dolor sit amet, consectetur adipiscing elit, sed do eiusmod tempor incididunt ut labore et dolore magna aliqua. Quis ipsum suspendisse ultrices gravida. Risus commodo viverra maecenas acc</p>
  <div class="reviewer"><span class="avatar"></span><div><b>Robert Jameson</b><span class="stars">★★★★★</span></div></div>
  <span class="source"></span>
</article>

<!-- contact -->
<svg class="contact-bg abs" viewBox="0 0 1200 650" preserveAspectRatio="none">
  <defs><linearGradient id="ctGrad" x1="0" y1="0" x2="1" y2="0.3"><stop offset="0" stop-color="#7d2462"/><stop offset=".45" stop-color="#b43a6e"/><stop offset="1" stop-color="#ec7a3c"/></linearGradient></defs>
  <path d="M0 30 C 400 0 800 0 1200 40 L1200 620 C 800 640 400 620 0 540 Z" fill="url(#ctGrad)"/>
  <path d="M0 30 C 400 0 800 -4 1200 40 L1200 70 C 800 20 400 20 0 40 Z" fill="var(--orange)"/>
  <path d="M0 540 C 400 620 800 640 1200 620 L1200 650 L0 650 Z" fill="#fff"/>
  <path d="M0 525 C 400 605 800 625 1200 610 L1200 620 C 800 640 400 620 0 545 Z" fill="var(--amber)"/>
</svg>
<div class="contact-line abs"></div>
<div class="eyebrow contact-eyebrow abs" id="contact">Get In Touch</div>
<h2 class="contact-title abs">Contact Us</h2>
<div class="field abs" style="top:3170px;height:46px">Name*</div>
<div class="field abs" style="top:3225px;height:45px">Email address*</div>
<div class="field abs" style="top:3278px;height:47px">Subject*</div>
<div class="field abs" style="top:3334px;height:91px">Message</div>
<a class="btn btn-send abs" href="#contact">SEND MESSAGE</a>
<div class="contact-art abs" role="img" aria-label="Speech bubble collage with photos of people talking and a tree silhouette"></div>

<!-- footer -->
<div class="brand footer-brand abs"><span class="brand-dot"></span>Dr Clara Vance</div>
<div class="socials abs"><span role="img" aria-label="Social profile 1"></span><span role="img" aria-label="Social profile 2"></span><span role="img" aria-label="Social profile 3"></span></div>
<div class="divider abs" style="left:508px"></div>
<div class="divider abs" style="left:755px"></div>
<div class="f-head abs" style="left:510px;top:3692px">Quick Links</div>
<ul class="f-links abs">
  <li>Home</li><li>About Us</li><li>Services</li><li>Fees &amp; Information</li><li>Contact Us</li>
</ul>
<div class="f-head abs" style="left:757px;top:3692px">Contact Us</div>
<div class="f-contact abs">
  <div class="f-row"><span class="f-icon"><svg width="20" height="20" viewBox="0 0 24 24"><path d="M6.6 10.8a15 15 0 0 0 6.6 6.6l2.2-2.2a1 1 0 0 1 1-.25 11 11 0 0 0 3.6.6 1 1 0 0 1 1 1V20a1 1 0 0 1-1 1A17 17 0 0 1 3 4a1 1 0 0 1 1-1h3.5a1 1 0 0 1 1 1c0 1.25.2 2.45.6 3.6a1 1 0 0 1-.25 1z" fill="#fff"/></svg></span><div>Phone Number<br><b style="font-weight:600">(555) 014-2768</b></div></div>
  <div class="f-row"><span class="f-icon"><svg width="20" height="20" viewBox="0 0 24 24"><rect x="3" y="5" width="18" height="14" rx="2" fill="#fff"/><path d="M3 7l9 6 9-6" fill="none" stroke="#e88bb3" stroke-width="2"/></svg></span><div>Email address<br>info@claravancepractice.com</div></div>
</div>
<div class="footer-rule abs"></div>
<div class="copyright abs">© 2024 Dr Clara Vance. All Rights Reserved</div>

</body>
</html>
```